Window Perf design with eadership quotes

I am wanting to create a window perf that covers windows in a conference room. I have included a picture of the windows. Each window is 26 1/2 inches by 92 inches. I have also included several other pictures to give an example of how I would like the Quotes to look.

Some Quotes I would like to use
1. Your Future is created by what you do today not tomorrow.
2. The answer is Yes
3. People don't care how much you know until they know how much you care.
4. Treat employees like they make a difference and they will.
5. Don't follow the crowd, Let the crowd follow you.
6. Treat people as if they were what they ought to be , and help them become what they are capable of being.
7. Leadership is not a title, its a behavior. LIVE IT
8. We make a living by what we get, We make a life by what we give.
9. Success is not final, failure is not fatal: it is courage to continue that counts.
10. The best way to predict your future is to create it.
11. The supreme quality of leadership is Integrity.
12. Whatever you are, Be a good one

Quotes

• I am imore interested in how this looks rather than including all of the quotes. I also ant this to be a solid background design for privacy.

```html
<!DOCTYPE html>
<html lang="en">
<head>
<meta charset="utf-8">
<title>Leadership Quotes – Window Perf Panels</title>
<link rel="stylesheet" href="https://fonts.googleapis.com/css2?family=Anton&family=Courier+Prime:wght@700&family=Encode+Sans+Condensed:wght@500&family=Lobster&family=Oswald:wght@700&family=Yellowtail&display=swap">
<style>
  :root {
    --page: #ecebe6;
    --panel: #0c0c0c;
    --yellow: #f6c500;
    --red: #e2232f;
    --white: #ffffff;
    --ink: #0c0c0c;
  }
  * { box-sizing: border-box; margin: 0; padding: 0; }
  html, body { width: 1200px; height: 864px; overflow: hidden; background: var(--page); }
  .window-set {
    position: relative;
    width: 1200px; height: 864px;
    display: flex; justify-content: center; align-items: center;
    gap: 22px;
  }
  .panel {
    position: relative;
    width: 225px; height: 780px;
    background: var(--panel);
  }

  /* Panel 1 – highlighted block quote */
  .quote-ideas {
    position: absolute; left: 16px; top: 264px;
    font-family: "Anton", "Oswald", sans-serif;
    font-size: 29px; line-height: 1;
    text-transform: uppercase;
  }
  .quote-ideas .tag {
    display: block; width: fit-content;
    padding: 4px 4px 3px;
    margin-bottom: 5px;
  }
  .quote-ideas .tag--red { background: var(--red); color: var(--white); }
  .quote-ideas .tag--yellow { background: var(--yellow); color: var(--ink); }

  /* Panel 2 – typewriter quote */
  .quote-future {
    position: absolute; left: 22px; top: 258px;
    font-family: "Courier Prime", "Courier New", monospace;
    font-weight: 700; font-size: 27px; line-height: 42px;
    color: var(--yellow);
    text-transform: uppercase;
  }
  .quote-future .accent { color: var(--white); }

  /* Panel 3 – centred mixed quote */
  .quote-predict {
    position: absolute; left: 0; right: 0; top: 250px;
    display: flex; flex-direction: column; align-items: center;
    font-family: "Encode Sans Condensed", "Arial Narrow", sans-serif;
    font-weight: 500; color: var(--white);
    text-transform: uppercase; text-align: center;
  }
  .quote-predict .line { font-size: 31px; line-height: 40px; letter-spacing: -0.5px; }
  .quote-predict .line--small { font-size: 25px; line-height: 36px; }
  .quote-predict .script {
    font-family: "Lobster", cursive;
    font-size: 50px; line-height: 62px;
    text-transform: none;
  }
  .quote-predict .script--red { color: var(--red); }
  .quote-predict .script--yellow { color: var(--yellow); }

  /* Panel 4 – script and bold */
  .quote-good-one {
    position: absolute; left: 0; right: 0; top: 300px;
    display: flex; flex-direction: column; align-items: center;
    color: var(--yellow); text-align: center;
  }
  .quote-good-one .script {
    font-family: "Yellowtail", cursive;
    font-size: 42px; line-height: 52px;
  }
  .quote-good-one .script--small { font-size: 34px; line-height: 48px; }
  .quote-good-one .bold {
    font-family: "Oswald", "Arial Narrow", sans-serif;
    font-weight: 700; font-size: 47px; line-height: 56px;
    text-transform: uppercase;
  }
</style>
</head>
<body>
  <main class="window-set">
    <section class="panel panel--ideas">
      <p class="quote-ideas">
        <span class="tag tag--red">It’s not</span>
        <span class="tag tag--red">about ideas.</span>
        <span class="tag tag--yellow">It’s about</span>
        <span class="tag tag--yellow">making</span>
        <span class="tag tag--yellow">ideas</span>
        <span class="tag tag--yellow">happen.</span>
      </p>
    </section>

    <section class="panel panel--future">
      <p class="quote-future">
        Your<br>future is<br>created<br>by what<br>you do<br>today, <span class="accent">not</span><br><span class="accent">tomorrow.</span>
      </p>
    </section>

    <section class="panel panel--predict">
      <p class="quote-predict">
        <span class="line">The best way</span>
        <span class="line line--small">to</span>
        <span class="script script--red">Predict</span>
        <span class="line">The future</span>
        <span class="line line--small">is to</span>
        <span class="script script--yellow">Create</span>
        <span class="line line--small">it</span>
      </p>
    </section>

    <section class="panel panel--good-one">
      <p class="quote-good-one">
        <span class="script">Whatever</span>
        <span class="bold">You are</span>
        <span class="script script--small">- be a -</span>
        <span class="bold">Good one</span>
      </p>
    </section>
  </main>
</body>
</html>
```